MARVELTRUST web-presence redisign

We would like to have our existing web-presence redesigned. Have a look at www.pelbrika-example.ch (please use explorer). To the existing 11 pages we would add one more.

```html
<!DOCTYPE html>
<html lang="en">
<head>
<meta charset="utf-8">
<title>MARVELTRUST Zahnarztpraxis</title>
<link href="https://fonts.googleapis.com/css2?family=Roboto:wght@400;500&family=Oswald:wght@500&display=swap" rel="stylesheet">
<style>
:root{
  --navy:#14125a;
  --navy-deep:#0c0b44;
  --gold:#f2c45c;
  --gold-dark:#d9a24d;
  --gold-text:#f0c060;
  --text:#6d6d6d;
  --line:#dcdcdc;
  --white:#fff;
}
*{margin:0;padding:0;box-sizing:border-box}
html,body{width:850px;height:1200px;overflow:hidden}
body{position:relative;background:var(--white);font-family:'Roboto',Arial,sans-serif;color:var(--text)}
.abs{position:absolute}
.header{left:0;top:0;width:850px;height:81px;background:linear-gradient(90deg,#cfcfcf,#dcdcdc 40%,#d3d3d3)}
.brand{left:76px;top:22px;display:flex;align-items:center;gap:8px}
.brand-mark{width:22px;height:22px;border-radius:50%;background:var(--gold-dark)}
.brand-name{font-size:20px;font-weight:500;color:#6a6a6a;letter-spacing:1px}
.lang{left:654px;top:18px;font-size:10px;color:#444;display:flex;align-items:center;gap:6px}
.flag{width:28px;height:14px;display:block}
.call{right:93px;top:50px;font-size:9.5px;color:#444;display:flex;align-items:baseline;gap:4px}
.call strong{font-size:14px;font-weight:500;color:var(--navy)}
.nav{left:0;top:81px;width:850px;height:33px;background:var(--gold)}
.nav a{position:absolute;top:0;height:33px;line-height:33px;font-size:11px;color:var(--white);text-decoration:none}
.nav .active{background:var(--gold-dark);padding:0 9px}
.search{left:597px;top:5px;width:160px;height:22px;border:1px solid #fbe7b8;font-size:7.5px;color:#fff8e6;padding:6px 5px}
.search svg{position:absolute;right:4px;top:3px}
.hero{left:0;top:114px;width:850px;height:333px;background:radial-gradient(ellipse at 70% 20%,#5a58a0,var(--navy) 55%,var(--navy-deep))}
.slide{left:93px;top:19px;width:664px;height:293px;background:linear-gradient(135deg,#d9cbb9,#eee8df 45%,#8fb4c0 75%,#ece9e6)}
.arrow{top:132px;width:24px;height:24px}
.welcome-title{left:93px;top:466px;font-size:21px;font-weight:400;color:var(--navy-deep)}
.para{left:94px;width:412px;font-size:8.6px;line-height:16.5px;color:#7a7a7a}
.photo{left:93px;top:633px;width:158px;height:133px;background:linear-gradient(135deg,#b89a78,#e8cdb3 50%,#c7a88d);border-radius:2px}
.list{list-style:none}
.list li{height:23px;line-height:22px;border-bottom:1px solid var(--line);font-size:9px;color:#444;padding-left:8px;position:relative;white-space:nowrap}
.list li::before{content:"";position:absolute;left:0;top:9px;border-left:3px solid #555;border-top:2px solid transparent;border-bottom:2px solid transparent}
.btn{left:306px;top:754px;width:72px;height:24px;background:var(--gold);color:var(--white);font-size:10.5px;line-height:24px;text-align:center}
.divider{left:530px;top:470px;width:1px;height:316px;background:var(--line)}
.news-title{left:561px;top:467px;font-size:11.5px;font-weight:400;color:var(--navy-deep)}
.news-rule{left:561px;top:492px;width:196px;height:1px;background:var(--line)}
.more-link{left:570px;top:625px;font-size:10px;color:var(--gold-text)}
.banner{left:562px;top:654px;width:195px;height:125px;background:linear-gradient(135deg,#5e5e5e,#7a716e 60%,#5c5858);text-align:center;color:var(--white);overflow:hidden}
.banner h2{font-family:'Oswald',sans-serif;font-weight:500;font-size:18px;line-height:32px;margin-top:17px;white-space:nowrap;letter-spacing:0}
.banner span{display:block;margin-top:5px;font-size:10.5px}
.rule{left:93px;width:664px;height:1px;background:var(--line)}
.works-title{left:93px;top:808px;font-size:21px;font-weight:400;color:var(--navy-deep)}
.work{width:366px;height:101px}
.work .thumb{position:absolute;left:0;top:0;width:126px;height:101px}
.work h3{position:absolute;left:137px;top:0;font-size:13px;font-weight:400;color:var(--gold-text);white-space:nowrap}
.work p{position:absolute;left:137px;top:22px;width:182px;font-size:7.8px;line-height:14.5px;color:#777}
.work .read{position:absolute;left:137px;top:74px;font-size:8.5px;color:#222}
.footer{left:0;top:1128px;width:850px;height:72px;background:var(--navy-deep)}
.foot-nav{left:93px;top:21px;font-size:9.5px;color:var(--white);display:flex}
.foot-nav span{margin-right:16px}
.copy{left:93px;top:49px;font-size:8px;color:#d6d6e6}
.connect{left:526px;top:30px;font-size:12.5px;color:var(--white)}
.social{left:630px;top:27px;display:flex;gap:5.5px}
.social i{display:block;width:21px;height:21px;border-radius:50%;background:var(--white)}
</style>
</head>
<body>
<header class="abs header">
  <div class="abs brand"><span class="brand-mark"></span><span class="brand-name">MARVELTRUST</span></div>
  <div class="abs lang">Language
    <svg class="flag" viewBox="0 0 28 14"><rect width="28" height="14" fill="#1f2f7a"/><rect x="11" width="6" height="14" fill="#fff"/><rect y="4" width="28" height="6" fill="#fff"/><rect x="12" width="4" height="14" fill="#c8102e"/><rect y="5" width="28" height="4" fill="#c8102e"/></svg>
    <svg class="flag" viewBox="0 0 28 14"><rect width="28" height="5" fill="#111"/><rect y="5" width="28" height="4" fill="#d00"/><rect y="9" width="28" height="5" fill="#ffce00"/></svg>
  </div>
  <div class="abs call"><svg width="9" height="9" viewBox="0 0 10 10"><path d="M2 1l2 2-1 1.5c.7 1.3 1.6 2.2 2.5 2.5L7 6l2 2-1.5 1.5C4.5 9.5.5 5.5.5 2.5z" fill="#555"/></svg>Call Us: <strong>41 (0)44 555 01 23</strong></div>
</header>

<nav class="abs nav">
  <a class="active" style="left:93px">HOME</a>
  <a style="left:160px">ZAHNMEDIZIN</a>
  <a style="left:258px">DENTALHYGIENE</a>
  <a style="left:388px">TEAM</a>
  <a style="left:442px">KONTAKT</a>
  <div class="abs search">Enter any Keywords....
    <svg width="14" height="14" viewBox="0 0 14 14"><circle cx="5.5" cy="5.5" r="4" fill="none" stroke="#fff" stroke-width="1.6"/><path d="M8.5 8.5l4 4" stroke="#fff" stroke-width="2"/></svg>
  </div>
</nav>

<section class="abs hero">
  <div class="abs slide" role="img" aria-label="Dentist in blue gloves examining a smiling girl in a dental chair"></div>
  <svg class="abs arrow" style="left:97px" viewBox="0 0 24 24"><circle cx="12" cy="12" r="11" fill="rgba(0,0,0,.25)" stroke="#fff" stroke-width="2"/><path d="M14 7l-5 5 5 5" fill="none" stroke="#fff" stroke-width="2.5"/></svg>
  <svg class="abs arrow" style="left:730px" viewBox="0 0 24 24"><circle cx="12" cy="12" r="11" fill="rgba(0,0,0,.25)" stroke="#fff" stroke-width="2"/><path d="M10 7l5 5-5 5" fill="none" stroke="#fff" stroke-width="2.5"/></svg>
</section>

<h1 class="abs welcome-title">Welcome To Our Website!</h1>
<p class="abs para" style="top:498px">K&amp;R Services was a division of the Harwick and Bellamy Company and was established in 1djhj979 with the initial intent of recovering the Phosphate value of co-product 35% Phosphoric Acid frcbbhom aluminum anodizing. Trisodium Phosphate was derived from th........</p>
<p class="abs para" style="top:561px">The assets of K&amp;R Services were purchased in September 1993 by Martin Feld and incorphbjcforated thereafter as K&amp;R Chemicals, Inc. K &amp; R Chemicals blends and distributes dry and wet products. et prod. These items are packaged in bags.......................,</p>
<div class="abs photo" role="img" aria-label="Portrait of a smiling woman"></div>
<ul class="abs list" style="left:305px;top:622px;width:191px">
  <li>Our core business</li><li>Leadership, direction and dedicated,</li><li>Focussed attention managementf-</li><li>gudgfyguhfgh</li><li>Resourcing solutions</li>
</ul>
<div class="abs btn">Read More</div>

<div class="abs divider"></div>
<h2 class="abs news-title">Our Dental News</h2>
<div class="abs news-rule"></div>
<ul class="abs list" style="left:561px;top:499px;width:196px">
  <li>Our core business</li><li>Leadership, direction and dedi-</li><li>cated, Focussed attention manage-</li><li>mentfgudgfyguhfgh</li><li>Resourcing solutions</li>
</ul>
<div class="abs more-link">Read More ▾</div>
<div class="abs banner" role="img" aria-label="Faded smile photo behind welcome message"><h2>HERZLICH WILLKOMMEN<br>IN UNSERER NEUEN</h2><span>Read More</span></div>

<div class="abs rule" style="top:794px"></div>
<h2 class="abs works-title">Our Works</h2>

<article class="abs work" style="left:93px;top:846px"><div class="thumb" role="img" aria-label="Dental mirror checking a patient's teeth" style="background:linear-gradient(135deg,#e9d6c6,#c79b83 55%,#f1ece7)"></div><h3>Lorem Ipsum dolore Site</h3><p>Nullam arcu velit, commodo non mi quis, varius dignissim turpis. Donec rutrum rhoncus ipsum, quis luctus nulla vestibulu</p><span class="read">{Read More}</span></article>
<article class="abs work" style="left:444px;top:846px"><div class="thumb" role="img" aria-label="Close-up of a bright white smile" style="background:linear-gradient(135deg,#f2c9ae,#e29a85 55%,#f5d7c4)"></div><h3>Lorem Ipsum dolore Site</h3><p>Nullam arcu velit, commodo non mi quis, varius dignissim turpis. Donec rutrum rhoncus ipsum, quis luctus nulla vestibulu</p><span class="read">{Read More}</span></article>
<article class="abs work" style="left:93px;top:982px"><div class="thumb" role="img" aria-label="Patient having a dental check-up" style="background:linear-gradient(135deg,#8ec5e3,#e6d1c3 50%,#f3f3f3)"></div><h3>Lorem Ipsum dolore Site</h3><p>Nullam arcu velit, commodo non mi quis, varius dignissim turpis. Donec rutrum rhoncus ipsum, quis luctus nulla vestibulu</p><span class="read">{Read More}</span></article>
<article class="abs work" style="left:444px;top:982px"><div class="thumb" role="img" aria-label="Child at a dental examination" style="background:linear-gradient(135deg,#6b4c36,#d9b69a 50%,#cfe3e6)"></div><h3>Lorem Ipsum dolore Site</h3><p>Nullam arcu velit, commodo non mi quis, varius dignissim turpis. Donec rutrum rhoncus ipsum, quis luctus nulla vestibulu</p><span class="read">{Read More}</span></article>

<div class="abs rule" style="top:1105px"></div>

<footer class="abs footer">
  <div class="abs foot-nav"><span>HOME</span><span>ZAHNMEDIZIN</span><span style="margin-right:9px">DENTALHYGIENE</span><span style="margin-right:12px">TEAM</span><span>KONTAKT</span></div>
  <div class="abs copy">© 2014 all copy rights are reserved</div>
  <div class="abs connect">Connect With Us</div>
  <div class="abs social"><i></i><i></i><i></i><i></i><i></i></div>
</footer>
</body>
</html>
```